Kesar tadka food truck catering business card

Need business card for indian restaurant - food truck- catering business
Updates

Reason: Just launched

Updated picture of new logo we need on business card

please see new LOGO in picture brief, need card with NEW LOGO

Industry/Entity Type

Indian Restaurant

Requirements
Must have
• Food truck. Catering

Owner Gurmeet Dhaliwal
Cell: 555-013-7284
Charleston,SC
www.KesarTadkaEats.com
www.plazaface.net/KesarTadkaEats

```html
<!DOCTYPE html>
<html lang="en">
<head>
<meta charset="utf-8">
<title>Kesar tadka – Business Card</title>
<link rel="stylesheet" href="https://fonts.googleapis.com/css2?family=Arimo:wght@400;700&display=swap">
<style>
  :root {
    --page-bg: #e9e7e4;
    --card-black: #272425;
    --lime: #8dc63f;
    --plum: #6a1b4d;
    --ink-dark: #1f1c1d;
    --ink-light: #ffffff;
  }
  html, body {
    margin: 0;
    width: 1200px;
    height: 918px;
    overflow: hidden;
    background: var(--page-bg);
    font-family: "Arimo", Arial, sans-serif;
  }
  .card {
    position: absolute;
    left: 100px;
    top: 173px;
    width: 1000px;
    height: 572px;
    background: var(--card-black);
    overflow: hidden;
    box-shadow: 0 6px 24px rgba(0,0,0,0.18);
  }
  .name-band {
    position: absolute;
    left: 0;
    top: 206px;
    width: 318px;
    height: 76px;
    background: var(--lime);
    text-align: right;
    box-sizing: border-box;
    padding: 8px 22px 0 0;
  }
  .owner-name {
    font-size: 31px;
    color: var(--ink-dark);
    line-height: 1.1;
  }
  .owner-title {
    font-size: 24px;
    color: var(--plum);
    line-height: 1.1;
  }
  .brand {
    position: absolute;
    left: 348px;
    top: 204px;
  }
  .brand-row {
    display: flex;
    align-items: center;
    gap: 18px;
  }
  .brand-name {
    font-size: 56px;
    font-weight: 700;
    color: var(--lime);
    line-height: 1;
    letter-spacing: -0.5px;
  }
  .brand-mark {
    width: 62px;
    height: 62px;
    background: var(--plum);
  }
  .brand-tagline {
    margin-top: 6px;
    font-size: 21px;
    color: var(--ink-light);
  }
  .contact-band {
    position: absolute;
    left: 0;
    bottom: 0;
    width: 1000px;
    height: 160px;
    background: var(--lime);
  }
  .address-block {
    position: absolute;
    right: 0;
    bottom: 72px;
    width: 430px;
    height: 130px;
    background: var(--card-black);
    box-sizing: border-box;
    padding: 36px 0 0 40px;
    color: var(--ink-light);
    font-size: 27px;
    line-height: 1.25;
  }
  .phone {
    position: absolute;
    left: 26px;
    bottom: 108px;
    font-size: 20px;
    color: var(--ink-dark);
  }
  .website {
    position: absolute;
    left: 186px;
    bottom: 82px;
    font-size: 20px;
    color: var(--ink-dark);
  }
  .social {
    position: absolute;
    right: 26px;
    bottom: 26px;
    font-size: 20px;
    color: var(--ink-dark);
  }
</style>
</head>
<body>
  <main class="card">
    <div class="name-band">
      <div class="owner-name">Gurmeet Dhaliwal</div>
      <div class="owner-title">Owner</div>
    </div>

    <div class="brand">
      <div class="brand-row">
        <span class="brand-name">Kesar tadka</span>
        <span class="brand-mark" aria-hidden="true"></span>
      </div>
      <div class="brand-tagline">Food truck. Catering</div>
    </div>

    <div class="contact-band"></div>
    <div class="address-block">
      2750 Harbor Mill Rd<br>
      Charleston, South Carolina
    </div>
    <div class="phone">555-013-7284</div>
    <div class="website">www.KesarTadkaEats.com</div>
    <div class="social">www.plazaface.net/KesarTadkaEats</div>
  </main>
</body>
</html>
```